Clever & creative business card needed for a pediatric dentist.

We need a business card for a pediatric dentist that is building a brand-new pediatric dental practice. He is funny, outgoing, and sociable, and he hopes to give his business card to dentists and pediatricians so that he can give them information of where to refer infants, children, and teenagers that need high quality and attainable dental care.

The name of the dental practice is Amber Creek Pediatric Dentistry. Logo design .png / .pdf/ .jpg are provided to aid in the design.

The dentist's last name is Moffat (which sounds like "burger", as in "hamburger” or “cheeseburger"). Since it is pediatric practice, kudos will be given to designs that implement a little joke into the design - but hopefully in a small or hidden way (such as putting something like a cheeseburger on the back of the card, or hiding it an an abstract way).

Thank you!

Please make a design that incorporates colors. It should be fun! Not too serious. It does not have to follow the color scheme of the logos.

```html
<!DOCTYPE html>
<html lang="en">
<head>
<meta charset="utf-8">
<title>Amber Creek Pediatric Dentistry – Business Card</title>
<link rel="stylesheet" href="https://fonts.googleapis.com/css2?family=Montserrat:wght@400;500;600;700&display=swap">
<style>
  :root{
    --page:#e6e7e6;
    --card-white:#ffffff;
    --card-dark:#3a3a3a;
    --ink:#2f2f2f;
    --ink-soft:#4a4a4a;
    --green:#5cb86a;
    --green-deep:#2f9a4c;
    --green-pale:#c6e3bf;
    --on-dark:#ffffff;
  }
  *{box-sizing:border-box;margin:0;padding:0}
  html,body{width:1200px;height:1186px;overflow:hidden}
  body{
    background:var(--page);
    font-family:"Montserrat",sans-serif;
    display:flex;flex-direction:column;align-items:center;justify-content:center;gap:56px;
  }
  .card{
    width:900px;height:514px;border-radius:36px;position:relative;overflow:hidden;
    box-shadow:0 10px 30px rgba(0,0,0,.18);
  }
  /* front */
  .card--front{background:var(--card-white);color:var(--ink)}
  .front__brand{
    position:absolute;left:70px;top:72px;width:440px;
    font-weight:600;color:var(--ink);
  }
  .front__brand .brand-name{font-size:48px;line-height:1;letter-spacing:.5px;text-transform:lowercase}
  .front__brand .brand-sub{font-size:19px;letter-spacing:6px;text-transform:uppercase;margin-top:10px}
  .front__mark{
    position:absolute;right:90px;top:60px;width:270px;height:270px;border-radius:50%;
    background:var(--green-pale);
  }
  .person{position:absolute;left:70px;top:236px}
  .person__name{font-size:30px;font-weight:700;color:var(--green)}
  .person__role{font-size:18px;font-weight:500;color:var(--ink);margin-top:4px}
  .contact{position:absolute;left:70px;top:330px;list-style:none;font-size:18px;font-weight:500;color:var(--ink-soft)}
  .contact li{display:flex;align-items:center;gap:14px;height:30px}
  .contact svg{width:18px;height:18px;fill:var(--green-deep)}
  .address{position:absolute;left:70px;top:438px;font-size:18px;font-weight:500;line-height:1.3;color:var(--ink)}
  /* back */
  .card--back{background:var(--card-dark);color:var(--on-dark);display:flex;flex-direction:column;align-items:center;justify-content:center}
  .back__mark{width:170px;height:170px;border-radius:50%;background:var(--green);margin-bottom:30px}
  .back__brand{text-align:center;font-weight:600;color:var(--on-dark)}
  .back__brand .brand-name{font-size:68px;line-height:1;text-transform:lowercase;letter-spacing:1px}
  .back__brand .brand-sub{font-size:24px;letter-spacing:9px;text-transform:uppercase;margin-top:12px}
</style>
</head>
<body>

  <section class="card card--front" aria-label="Card front">
    <div class="front__brand">
      <div class="brand-name">amber creek</div>
      <div class="brand-sub">Pediatric Dentistry</div>
    </div>
    <div class="front__mark" aria-hidden="true"></div>

    <div class="person">
      <div class="person__name">Jonah Moffat</div>
      <div class="person__role">CEO &amp; Founder</div>
    </div>

    <ul class="contact">
      <li>
        <svg viewBox="0 0 24 24" aria-hidden="true"><path d="M6.6 10.8a15.1 15.1 0 0 0 6.6 6.6l2.2-2.2a1 1 0 0 1 1-.25 11.4 11.4 0 0 0 3.6.57 1 1 0 0 1 1 1V20a1 1 0 0 1-1 1A17 17 0 0 1 3 4a1 1 0 0 1 1-1h3.5a1 1 0 0 1 1 1c0 1.25.2 2.45.57 3.57a1 1 0 0 1-.25 1z"/></svg>
        555 21 40 88
      </li>
      <li>
        <svg viewBox="0 0 24 24" aria-hidden="true"><path d="M3 5h18a1 1 0 0 1 1 1v12a1 1 0 0 1-1 1H3a1 1 0 0 1-1-1V6a1 1 0 0 1 1-1zm9 7.5L20 7H4z"/></svg>
        info@ambercreekdental.com
      </li>
      <li>
        <svg viewBox="0 0 24 24" aria-hidden="true"><circle cx="12" cy="12" r="10"/></svg>
        www.ambercreekdental.com
      </li>
    </ul>

    <p class="address">Harbor Park, Suite 3 nº 2 8<br>2741 Riverside Vale</p>
  </section>

  <section class="card card--back" aria-label="Card back">
    <div class="back__mark" aria-hidden="true"></div>
    <div class="back__brand">
      <div class="brand-name">amber creek</div>
      <div class="brand-sub">Pediatric Dentistry</div>
    </div>
  </section>

</body>
</html>
```